Children's Chorus Flyer

Hello,

I need a flyer design (probably in two sizes 8x11, 5x7) that promotes my community children's chorus and also announces our summer camp. I would like a flyer that is playful and eye-catching while remaining somewhat simplistic. It should have our logo (will upload that) and either some cartoon graphics or pictures of the current kids or both. Although it does not have to have the picture of the kids. I'm leaving it up to you. I am uploading an example of a flyer that I like to help guide you. It needs to have this basic info:

"Do you love to sing? The Meadowlark Singers is looking for boys and girls ages 7-16 to audition for the 2012-2013 season! Rehearsals are held weekly at Birchfield Grove Methodist Church (27815 Hennaway Ln). Contact us for an audition appointment.

Summer Choral Camp!
The Meadowlark Singers is planning a 2-week choral camp where singers will have fun working on music reading skills, vocal technique, choreography and more! Boys and girls ages 7-16 are invited to enroll.

Dates: July 16-27
Times: 9am-3pm (extended care hours available at additional fee)
Tuition: $300 for 2-week session ($150 per week)

For more information, please visit our website: www.meadowlarksingers.org, email: info@meadowlarksingers.org or call 555.384.9127."

Target Market(s)

parents and children

Industry/Entity Type

Church

Requirements
Must have
• logo, basic info typed above.
Nice to have
• the picture of the kids, although not totally necessary. Leaving it up to your creative ideas.

```html
<!DOCTYPE html>
<html lang="en">
<head>
<meta charset="utf-8">
<title>The Meadowlark Singers – Auditions &amp; Summer Choral Camp</title>
<link href="https://fonts.googleapis.com/css2?family=Varela+Round&family=Fredoka:wght@600&display=swap" rel="stylesheet">
<style>
  :root {
    --blue: #3f5fe6;
    --magenta: #e23fe0;
    --green: #7df23e;
    --paper: #ffffff;
    --teal: #3aa58c;
    --shirt: #f4f6fc;
    --scarf: #5a78e8;
    --navy: #1e2033;
  }
  * { margin: 0; padding: 0; box-sizing: border-box; }
  html, body { width: 850px; height: 1200px; overflow: hidden; background: var(--paper); }
  .flyer {
    position: relative;
    width: 850px; height: 1200px;
    background: var(--paper);
    font-family: "Varela Round", sans-serif;
    overflow: hidden;
  }
  .brush { position: absolute; left: 0; top: 0; display: block; }

  .headline {
    position: absolute; left: 24px; top: 10px; width: 816px; height: 88px;
    display: flex; align-items: center; justify-content: center;
    color: var(--magenta); font-size: 72px; font-weight: 400; letter-spacing: 2px;
  }

  .brand {
    position: absolute; left: 20px; top: 140px; width: 330px;
    display: flex; align-items: center; gap: 12px;
    color: var(--teal); font-size: 30px; line-height: 1.1;
  }
  .brand-dot { width: 34px; height: 34px; border-radius: 50%; background: var(--teal); flex: none; }

  .contact {
    position: absolute; left: 20px; top: 232px;
    color: var(--magenta); font-size: 17px; line-height: 23px;
  }
  .contact strong { font-family: "Fredoka", sans-serif; font-weight: 600; font-size: 18px; }

  .audition {
    position: absolute; left: 398px; top: 130px; width: 433px;
    text-align: right; color: var(--green);
  }
  .audition h2 { font-family: "Fredoka", sans-serif; font-weight: 600; font-size: 28px; line-height: 34px; margin-bottom: 2px; }
  .audition p { font-size: 20.5px; line-height: 28px; }
  .audition .place { margin-top: 22px; line-height: 31px; }
  .audition .cta { font-family: "Fredoka", sans-serif; font-weight: 600; font-size: 18.5px; line-height: 23px; margin-top: 10px; }

  .photo {
    position: absolute; left: 70px; top: 392px; width: 752px; height: 450px;
    background: linear-gradient(180deg,
      var(--paper) 0%,
      var(--shirt) 30%,
      #dfe5f8 46%,
      var(--scarf) 60%,
      #3a3f66 74%,
      var(--navy) 100%);
  }

  .camp {
    position: absolute; left: 44px; top: 872px; width: 770px;
    color: var(--green); transform: rotate(-3deg); transform-origin: left top;
  }
  .camp h2 { font-family: "Fredoka", sans-serif; font-weight: 600; font-size: 29px; line-height: 30px; }
  .camp p { font-size: 20px; line-height: 24px; }
  .camp strong { font-family: "Fredoka", sans-serif; font-weight: 600; }
  .camp .details { margin-top: 22px; }
  .camp .note { font-style: italic; font-size: 17px; line-height: 19px; }
  .camp .tuition { margin-top: 26px; }
  .camp .tuition em { font-size: 17px; }
</style>
</head>
<body>
<main class="flyer">

  <svg class="brush" width="850" height="1200" viewBox="0 0 850 1200" aria-hidden="true">
    <path fill="var(--blue)" d="M26 12 L300 8 L560 14 L838 10 L834 42 L840 72 L836 98 L560 102 L300 96 L24 100 L28 70 L22 40 Z"/>
    <path fill="var(--blue)" d="M394 118 L620 122 L840 116 L836 210 L842 300 L836 404 L620 398 L396 402 L392 300 L396 200 Z"/>
    <path fill="var(--blue)" d="M48 372 L400 366 L840 380 L836 600 L842 830 L48 842 L42 600 Z"/>
    <path fill="var(--blue)" d="M30 846 L420 830 L834 800 L838 980 L830 1154 L420 1160 L38 1172 L32 1000 Z"/>
  </svg>

  <h1 class="headline">do you love to sing?</h1>

  <div class="brand">
    <span class="brand-dot"></span>
    <span>The Meadowlark Singers</span>
  </div>

  <p class="contact">
    for more information<br>
    please visit our website:<br>
    <strong>www.meadowlarksingers.org</strong><br>
    email: <strong>info@meadowlarksingers.org</strong><br>
    or call: <strong>555 384 9127</strong>
  </p>

  <section class="audition">
    <h2>The Meadowlark Singers</h2>
    <p>is looking for boys and girls aged 7-16<br>to audition for the 2012-2013 season!</p>
    <p class="place">Rehearsals are held weekly at:<br>Birchfield Grove Methodist Church<br>(27815 Hennaway Ln)</p>
    <p class="cta">contact us for an<br>audition appointment</p>
  </section>

  <div class="photo" role="img" aria-label="Photo of the chorus children in white shirts, blue neckerchiefs and dark trousers, cheering with raised arms"></div>

  <section class="camp">
    <h2>Summer Choral Camp!</h2>
    <p>The Meadowlark Singers is planning a 2-week choral camp<br>where singers will have fun working on music reading<br>skills, vocal technique, choreography and more!<br><strong>Boys and girls ages 7-16</strong> are invited to enroll.</p>
    <p class="details">Dates: <strong>July 16-27</strong><br>Times: <strong>9.00am-3.00 pm</strong></p>
    <p class="note">(extended care hours available at additional fee)</p>
    <p class="tuition">Tuition: <strong>$300 for 2-week session</strong> <em>($150 per week)</em></p>
  </section>

</main>
</body>
</html>
```